Maple Grove Schools | brand new stationery!

We need stationery design with our new logo! Our company updated it's name and image and we like to incorporate the new one on our stationery, business cards and email signature. We are looking for fresh, new ideas!
Industry: Childcare, Elementary and Middle School
Company Name: Maple Grove Schools
Tagline: Bright Futures Start Here
Main colors: Blue, white and a little yellow
Star shape is something new for us! Do you see a way to incorporate it as a design element?

```html
<!DOCTYPE html>
<html lang="en">
<head>
<meta charset="utf-8">
<title>Maple Grove Schools – Business Card</title>
<link href="https://fonts.googleapis.com/css2?family=Montserrat:wght@800&family=Poppins:wght@400;600&display=swap" rel="stylesheet">
<style>
  :root {
    --backdrop: #c4c4c4;
    --paper: #f2f2f2;
    --ink: #2b2a2a;
    --charcoal: #2f2c2d;
    --brand-blue: #1b2a80;
    --star-yellow: #f2bf2a;
    --white: #ffffff;
  }
  html, body {
    margin: 0;
    width: 1200px;
    height: 800px;
    overflow: hidden;
    background: var(--backdrop);
  }
  .canvas {
    position: relative;
    width: 1200px;
    height: 800px;
  }
  .card {
    position: absolute;
    top: 340px;
    width: 480px;
    height: 275px;
    overflow: hidden;
    box-sizing: border-box;
  }
  .card--front { left: 96px; background: var(--paper); }
  .card--back  { left: 612px; background: var(--charcoal); }

  .brand-block {
    position: absolute;
    width: 210px;
    height: 210px;
    border-radius: 50%;
    background: var(--brand-blue);
  }
  .card--front .brand-block { right: -105px; top: 40px; }
  .card--back  .brand-block { left: -110px; top: 30px; }

  .wordmark {
    font-family: "Poppins", sans-serif;
    font-weight: 600;
    line-height: 1.05;
    margin: 0;
  }
  .card--front .wordmark {
    position: absolute;
    left: 40px;
    top: 24px;
    font-size: 32px;
    color: var(--ink);
  }
  .card--back .wordmark {
    position: absolute;
    left: 170px;
    top: 88px;
    font-size: 40px;
    color: var(--white);
    text-align: center;
  }

  .holder-name {
    position: absolute;
    left: 42px;
    top: 110px;
    margin: 0;
    font-family: "Montserrat", sans-serif;
    font-weight: 800;
    font-size: 21px;
    letter-spacing: -0.5px;
    color: var(--brand-blue);
  }
  .holder-role {
    position: absolute;
    left: 42px;
    top: 137px;
    margin: 0;
    font-family: "Poppins", sans-serif;
    font-size: 13px;
    color: var(--ink);
  }
  .contact-list {
    position: absolute;
    left: 42px;
    top: 162px;
    margin: 0;
    padding: 0;
    list-style: none;
    font-family: "Poppins", sans-serif;
    font-size: 13px;
    color: var(--ink);
  }
  .contact-list li {
    display: flex;
    align-items: center;
    gap: 9px;
    height: 19px;
  }
  .contact-list svg { width: 12px; height: 12px; fill: var(--brand-blue); }
  .postal-address {
    position: absolute;
    left: 42px;
    top: 225px;
    margin: 0;
    font-family: "Poppins", sans-serif;
    font-style: normal;
    font-size: 13px;
    line-height: 18px;
    color: var(--ink);
  }
  .tagline {
    position: absolute;
    left: 140px;
    top: 210px;
    margin: 0;
    font-family: "Poppins", sans-serif;
    font-size: 22px;
    color: var(--star-yellow);
  }
</style>
</head>
<body>
<main class="canvas">
  <section class="card card--front">
    <div class="brand-block" aria-hidden="true"></div>
    <h1 class="wordmark">Maple Grove<br>Schools</h1>
    <h2 class="holder-name">DANIEL HARTLEY</h2>
    <p class="holder-role">Managing Director</p>
    <ul class="contact-list">
      <li><svg viewBox="0 0 24 24" aria-hidden="true"><path d="M6.6 10.8a15 15 0 0 0 6.6 6.6l2.2-2.2c.3-.3.7-.4 1-.2 1.1.4 2.3.6 3.6.6.6 0 1 .4 1 1V20c0 .6-.4 1-1 1A17 17 0 0 1 3 4c0-.6.4-1 1-1h3.5c.6 0 1 .4 1 1 0 1.3.2 2.5.6 3.6.1.3 0 .7-.2 1z"/></svg>044-555 210 347</li>
      <li><svg viewBox="0 0 24 24" aria-hidden="true"><path d="M2 5h20v14H2zm2 2v.5l8 5 8-5V7l-8 5z"/></svg>hello@maplegroveschools.example</li>
      <li><svg viewBox="0 0 24 24" aria-hidden="true"><path d="M12 2a10 10 0 1 0 0 20 10 10 0 0 0 0-20zm0 2a8 8 0 0 1 7.7 6H15a13 13 0 0 0-2-5.9A8 8 0 0 1 12 4zm-1 .1A13 13 0 0 0 9 10H4.3A8 8 0 0 1 11 4.1zM4.3 12H9a13 13 0 0 0 2 7.9A8 8 0 0 1 4.3 12zm8.7 7.9a13 13 0 0 0 2-7.9h4.7a8 8 0 0 1-6.7 7.9z"/></svg>www.maplegroveschools.example</li>
    </ul>
    <address class="postal-address">18 Orchard Lane<br>Brookfield, 40318</address>
  </section>

  <section class="card card--back">
    <div class="brand-block" aria-hidden="true"></div>
    <h1 class="wordmark">Maple Grove<br>Schools</h1>
    <p class="tagline">Bright Futures Start Here</p>
  </section>
</main>
</body>
</html>
```